Halloway Consulting Cover 2 - Smart Capital

Halloway Consulting is a business consulting firm. We will publish a series of four thought leadership pieces online and via PDF. The second of the series is attached to this project. We need an eye-catching cover page with a back page that keeps with our branding. The document attached is in the final draft, and the cover and pack pages are placeholders only. You can find more about our branding and style on our website www.hallowayconsulting.com.au. The other three projects can be found here with a similar brief, and you are welcome to submit a design for all 4.

```html
<!DOCTYPE html>
<html lang="en">
<head>
<meta charset="utf-8">
<title>Halloway Consulting – Smart Capital Cover and Back Page</title>
<link rel="stylesheet" href="https://fonts.googleapis.com/css2?family=Barlow+Condensed:wght@600&family=Poppins:wght@400;500;600&display=swap">
<style>
  :root {
    --orange: #f28c28;
    --blue: #27a4e0;
    --ink: #2b2b2b;
    --charcoal-light: #444446;
    --charcoal-dark: #242425;
    --white: #ffffff;
    --rule: #3d8fb8;
  }
  * { margin: 0; padding: 0; box-sizing: border-box; }
  html, body { width: 1200px; height: 1200px; overflow: hidden; background: var(--white); }
  body { position: relative; font-family: "Poppins", sans-serif; color: var(--ink); }

  .page { position: absolute; top: 251px; width: 485px; height: 688px; background: var(--white); overflow: hidden; }
  .back-page { left: 111px; }
  .cover-page { left: 611px; }

  /* Back page */
  .back-panel {
    position: absolute; left: 0; top: 0; width: 100%; height: 498px;
    background: radial-gradient(ellipse at 30% 110%, var(--charcoal-dark) 0%, #2e2e2f 45%, var(--charcoal-light) 100%);
  }
  .brand { position: absolute; display: flex; align-items: center; gap: 6px; }
  .brand-dot { flex: none; width: 16px; height: 16px; border-radius: 50%; background: var(--orange); }
  .brand-name { font-weight: 600; color: var(--blue); line-height: 1; white-space: nowrap; }
  .back-brand { left: 42px; top: 520px; }
  .back-brand .brand-name { font-size: 12px; }
  .back-lede { position: absolute; left: 40px; top: 556px; font-size: 7.5px; font-weight: 500; line-height: 1.25; width: 220px; }
  .contact { position: absolute; top: 587px; font-size: 5.6px; line-height: 1.75; }
  .contact-one { left: 42px; }
  .contact-two { left: 171px; }
  .contact-name { font-weight: 600; }
  .contact-line { display: flex; align-items: center; gap: 3px; }
  .contact-line svg { width: 7px; height: 7px; }
  .back-url { position: absolute; left: 42px; top: 638px; font-size: 10px; color: var(--blue); }
  .follow { position: absolute; left: 330px; top: 638px; font-size: 9.5px; color: var(--blue); display: flex; align-items: center; gap: 10px; }
  .social-dot { width: 8px; height: 8px; border-radius: 50%; background: var(--blue); }

  /* Cover page */
  .cover-header { position: absolute; left: 0; top: 0; width: 100%; height: 121px; background: var(--white); }
  .cover-url { position: absolute; left: 40px; top: 53px; font-size: 12.5px; color: var(--ink); }
  .cover-brand { right: 30px; top: 50px; gap: 7px; }
  .cover-brand .brand-dot { width: 20px; height: 20px; }
  .cover-brand .brand-name { font-size: 14px; }
  .cover-photo {
    position: absolute; left: 0; top: 121px; width: 100%; height: 567px;
    background: linear-gradient(180deg, #2d3a52 0%, #54565f 22%, #7d6a5c 40%, #a36a45 55%, #5a3a33 68%, #1f2536 82%, #0c0d12 100%);
  }
  .cover-title {
    position: absolute; left: 40px; top: 172px;
    font-family: "Barlow Condensed", sans-serif; font-weight: 600;
    font-size: 54px; line-height: 52px; letter-spacing: -0.5px;
    text-transform: uppercase; color: var(--white);
  }
  .cover-title .accent { color: var(--orange); }
  .cover-subtitle { position: absolute; left: 41px; top: 408px; font-size: 13px; color: var(--white); }
  .cover-rule { position: absolute; left: 0; top: 651px; width: 100%; height: 1px; background: var(--rule); }
</style>
</head>
<body>

  <section class="page back-page">
    <div class="back-panel" role="img" aria-label="Dark charcoal panel with a large faint brand decoration"></div>

    <div class="brand back-brand">
      <span class="brand-dot"></span>
      <span class="brand-name">Halloway Consulting</span>
    </div>

    <p class="back-lede">Contact us to find out how Halloway Consulting can help build your company into a market leader today.</p>

    <div class="contact contact-one">
      <div class="contact-name">Daniel Halloway</div>
      <div>Managing Director</div>
      <div class="contact-line">
        <svg viewBox="0 0 10 10"><circle cx="5" cy="5" r="4.3" fill="none" stroke="#2b2b2b" stroke-width="0.9"/><path d="M3.4 3.1l1 1-0.5 0.6 1.4 1.4 0.6-0.5 1 1-0.7 0.7C5.3 7.2 2.8 4.7 2.8 3.8z" fill="#2b2b2b"/></svg>
        +61 400 318 205
      </div>
      <div class="contact-line">
        <svg viewBox="0 0 10 10"><circle cx="5" cy="5" r="4.3" fill="none" stroke="#2b2b2b" stroke-width="0.9"/><rect x="2.8" y="3.5" width="4.4" height="3" fill="#2b2b2b"/></svg>
        daniel@hallowayconsulting.com.au
      </div>
    </div>

    <div class="contact contact-two">
      <div class="contact-name">Marcus Halloway</div>
      <div>Managing Director</div>
      <div class="contact-line">
        <svg viewBox="0 0 10 10"><circle cx="5" cy="5" r="4.3" fill="none" stroke="#2b2b2b" stroke-width="0.9"/><path d="M3.4 3.1l1 1-0.5 0.6 1.4 1.4 0.6-0.5 1 1-0.7 0.7C5.3 7.2 2.8 4.7 2.8 3.8z" fill="#2b2b2b"/></svg>
        +61 400 627 914
      </div>
      <div class="contact-line">
        <svg viewBox="0 0 10 10"><circle cx="5" cy="5" r="4.3" fill="none" stroke="#2b2b2b" stroke-width="0.9"/><rect x="2.8" y="3.5" width="4.4" height="3" fill="#2b2b2b"/></svg>
        marcus@hallowayconsulting.com.au
      </div>
    </div>

    <div class="back-url">hallowayconsulting.com.au</div>
    <div class="follow">
      <span>Follow us</span>
      <span class="social-dot"></span>
      <span class="social-dot"></span>
    </div>
  </section>

  <section class="page cover-page">
    <header class="cover-header">
      <div class="cover-url">hallowayconsulting.com.au</div>
      <div class="brand cover-brand">
        <span class="brand-dot"></span>
        <span class="brand-name">Halloway Consulting</span>
      </div>
    </header>

    <div class="cover-photo" role="img" aria-label="Photograph of two hikers in silhouette on a mountain ridge at sunset, one helping the other climb up"></div>

    <h1 class="cover-title">
      <span class="accent">Smart Capital:</span><br>
      Partnering with<br>
      funds to scale<br>
      your business.
    </h1>
    <p class="cover-subtitle">Bridging valuation gaps in fund raising</p>
    <div class="cover-rule"></div>
  </section>

</body>
</html>
```